Website Design for Qolva-iX Software Solutions

Our company (IT) develops (3 main markets):
- Software for selfservice kiosks
- Web- and Mobile applications
- Embedded Software

```html
<!DOCTYPE html>
<html lang="en">
<head>
<meta charset="utf-8">
<title>Qolva-iX Software Solutions</title>
<link rel="stylesheet" href="https://fonts.googleapis.com/css2?family=Arimo:wght@400;700&display=swap">
<style>
  :root {
    --green: #8cc21c;
    --green-glow: #d8f0a0;
    --blue: #1f9fe0;
    --blue-dark: #1a86c4;
    --blue-deep: #136a9e;
    --footer: #1a8fcf;
    --accent: #2fa8e4;
    --card-top: #ffffff;
    --card-bottom: #ececec;
    --grey-text: #a4a4a4;
    --grey-head: #c9c9c9;
    --red: #c8161b;
    --red-dark: #8f0d10;
    --white-soft: #cfe9f8;
  }
  * { box-sizing: border-box; margin: 0; padding: 0; }
  html, body { width: 1200px; height: 1152px; overflow: hidden; }
  body {
    position: relative;
    background: var(--blue);
    font-family: "Arimo", Arial, sans-serif;
  }
  .site-header {
    position: absolute; left: 0; top: 0; width: 1200px; height: 104px;
    background: radial-gradient(ellipse 150px 90px at 600px 20px, var(--green-glow), var(--green) 100%);
    box-shadow: 0 3px 6px rgba(0,0,0,.18);
    display: flex; align-items: center; justify-content: center;
  }
  .brand {
    font-weight: 700; font-size: 46px; letter-spacing: 8px;
    color: #f07d1e; padding-top: 10px;
  }
  .services {
    position: absolute; left: 109px; top: 139px; width: 982px; height: 558px;
    border-radius: 8px;
    background: linear-gradient(var(--card-top), var(--card-bottom));
    box-shadow: 0 10px 24px rgba(0,0,0,.22);
  }
  .services::before {
    content: ""; position: absolute; left: 43px; right: 40px; top: 42px;
    border-top: 1px solid #e2e2e2;
  }
  .service {
    position: absolute; top: 60px; width: 320px; height: 470px;
    text-align: center;
  }
  .service + .service { border-left: 1px solid #e4e4e4; }
  .service:nth-child(1) { left: 2px; }
  .service:nth-child(2) { left: 322px; }
  .service:nth-child(3) { left: 642px; }
  .service-label {
    position: absolute; left: 24px; top: 6px; width: 220px; text-align: left;
    font-size: 21px; font-weight: 700; line-height: 28px;
    color: var(--grey-head);
    text-shadow: 0 1px 0 #fff, 0 -1px 0 #9a9a9a;
  }
  .service-mark {
    position: absolute; right: 30px; top: 10px; width: 32px; height: 32px;
    border-radius: 6px; background: #d2d2d2;
  }
  .service-icon {
    position: absolute; left: 94px; top: 96px; width: 133px; height: 133px;
    background: var(--accent); border-radius: 10px;
  }
  .service-title {
    position: absolute; left: 0; right: 0; top: 276px;
    font-size: 20px; font-weight: 400; color: var(--accent);
  }
  .service-text {
    position: absolute; left: 64px; right: 64px; top: 312px;
    font-size: 12px; line-height: 16px; color: var(--grey-text);
  }
  .read-more {
    position: absolute; left: 96px; top: 416px; width: 126px; height: 34px;
    border-radius: 5px;
    background: linear-gradient(#e52a2e, var(--red) 60%, #a81015);
    box-shadow: 0 4px 6px rgba(0,0,0,.3);
    color: #fff; font-size: 13px; line-height: 34px; text-align: left;
    padding-left: 12px; text-decoration: none;
  }
  .read-more::after {
    content: "+"; position: absolute; right: 0; top: 0; width: 28px; height: 34px;
    border-left: 1px solid var(--red-dark);
    text-align: center; font-size: 20px;
  }
  .clients-heading {
    position: absolute; left: 0; top: 758px; width: 1200px; text-align: center;
    font-size: 28px; font-weight: 700; color: var(--blue-dark);
    text-shadow: 0 1px 0 #5cc0f0, 0 -1px 0 #0f5f90;
  }
  .clients-heading::before, .clients-heading::after {
    content: ""; position: absolute; top: 18px; width: 440px;
    border-top: 1px solid #4db6ec;
  }
  .clients-heading::before { left: 28px; }
  .clients-heading::after { right: 28px; }
  .clients {
    position: absolute; left: 60px; top: 820px; width: 1080px; height: 110px;
    display: flex; align-items: center; justify-content: space-between;
    list-style: none;
  }
  .client {
    display: flex; align-items: center; gap: 8px;
    font-size: 26px; font-weight: 700; color: var(--blue-deep);
  }
  .client-dot { width: 22px; height: 22px; border-radius: 50%; background: var(--blue-deep); }
  .divider {
    position: absolute; left: 28px; right: 28px; top: 971px;
    border-top: 1px solid #4db6ec;
  }
  .disclaimer {
    position: absolute; left: 80px; width: 1040px; top: 998px; text-align: center;
    color: var(--white-soft);
  }
  .disclaimer h2 { font-size: 19px; font-weight: 400; margin-bottom: 14px; }
  .disclaimer p { font-size: 14px; line-height: 19px; }
  .site-footer {
    position: absolute; left: 0; top: 1104px; width: 1200px; height: 48px;
    background: var(--footer);
    border-top: 1px solid #3aaee8;
    color: var(--white-soft); font-size: 14px;
  }
  .copyright { position: absolute; left: 89px; top: 17px; }
  .footer-links {
    position: absolute; right: 40px; top: 17px;
    display: flex; align-items: center; gap: 26px; white-space: nowrap;
  }
  .footer-nav { display: flex; gap: 14px; font-size: 13px; }
  .social { display: flex; gap: 10px; font-size: 12px; }
</style>
</head>
<body>
  <header class="site-header">
    <div class="brand">QOLVA-IX</div>
  </header>

  <main class="services">
    <section class="service">
      <div class="service-label">KIOSKS</div>
      <div class="service-mark" role="img" aria-label="Small tools icon"></div>
      <div class="service-icon" role="img" aria-label="Wrench and screwdriver icon"></div>
      <h3 class="service-title">KIOSKS</h3>
      <p class="service-text">It is a long established fact that a reader will be distracted by the readable content of a page when looking at its layout</p>
      <a class="read-more" href="#">READ MORE</a>
    </section>
    <section class="service">
      <div class="service-label">Mobile and Web Applications</div>
      <div class="service-mark" role="img" aria-label="Small gear icon"></div>
      <div class="service-icon" role="img" aria-label="Two gears icon"></div>
      <h3 class="service-title">Web and Mobile Apps</h3>
      <p class="service-text">It is a long established fact that a reader will be distracted by the readable content of a page when looking at its layout</p>
      <a class="read-more" href="#">READ MORE</a>
    </section>
    <section class="service">
      <div class="service-label">Embedded Software</div>
      <div class="service-mark" role="img" aria-label="Small camera icon"></div>
      <div class="service-icon" role="img" aria-label="Video camera icon"></div>
      <h3 class="service-title">Embedded Software</h3>
      <p class="service-text">It is a long established fact that a reader will be distracted by the readable content of a page when looking at its layout</p>
      <a class="read-more" href="#">READ MORE</a>
    </section>
  </main>

  <h2 class="clients-heading">OUR CLIENTS</h2>
  <ul class="clients">
    <li class="client">Orchard</li>
    <li class="client">Brewline</li>
    <li class="client">Motora</li>
    <li class="client">Lumen TV</li>
    <li class="client"><span class="client-dot"></span>Vanta</li>
    <li class="client">Maison Clé</li>
    <li class="client"><span class="client-dot"></span>Voltaic</li>
  </ul>

  <div class="divider"></div>

  <section class="disclaimer">
    <h2>DISCLAIMER</h2>
    <p>It is a long established fact that a reader will be distracted by the readable content of a page when looking at its layout. The point of using Lorem Ipsum is that it has a more-or-less normal distribution of letters, as opposed to using 'Content here, content here', making it look like readable English</p>
  </section>

  <footer class="site-footer">
    <div class="copyright">© Copyright 2012, Qolva-iX. All Rights Reserved.</div>
    <div class="footer-links">
      <nav class="footer-nav">
        <span>KIOSCS</span>
        <span>WEB AND MOBILE APPS</span>
        <span>EMBEDDED SOFTWARE</span>
      </nav>
      <div class="social"><span>Birdcall</span><span>Pagebook</span></div>
    </div>
  </footer>
</body>
</html>
```